Cobbleford Works New Website

Custom Wood Cabinetry and Precisions Wood Cutting website. I have created a pdf document with all the specs for the project and attached it. I am just typing stuff in here so it stops telling me my description is too short. Their once was a man from Nantucket.. he used to pee in a bucket.. roses are red, cardinals are birds, i wish they didn't require 300 words.
Number of Pages Required
1 page

```html
<!DOCTYPE html>
<html lang="en">
<head>
<meta charset="utf-8">
<title>Cobbleford Works — Custom Cabinetry &amp; Woodworking</title>
<link rel="stylesheet" href="https://fonts.googleapis.com/css2?family=Figtree:wght@400;500;600;700&display=swap">
<style>
:root{
  --brown:#4a3324;
  --brown-dark:#3b2a1f;
  --ink:#2c2420;
  --muted:#5a514b;
  --sage:#87958a;
  --navy:#262a33;
  --footer:#ececec;
  --line:#8a7d74;
  --white:#fff;
}
*{box-sizing:border-box;margin:0;padding:0}
html,body{width:1200px;height:3101px;overflow:hidden}
body{position:relative;background:var(--white);font-family:"Figtree",sans-serif;color:var(--ink)}
.abs{position:absolute}
.center{text-align:center;left:0;width:1200px}

/* header */
.brand{left:200px;top:26px;font-size:17px;font-weight:700;color:var(--brown);display:flex;align-items:center;gap:7px;white-space:nowrap}
.brand-mark{width:12px;height:12px;border-radius:50%;background:var(--brown);flex:none}
.nav{font-size:11px;color:var(--muted)}
.nav a{position:absolute;color:inherit;text-decoration:none;white-space:nowrap}
.nav a.active{color:var(--brown);font-weight:600}
.call{left:742px;top:30px;font-size:12px;font-weight:600;color:var(--ink);white-space:nowrap}
.icon-btn{left:874px;top:22px;width:30px;height:30px;border:1.5px solid var(--brown);border-radius:50%;display:flex;align-items:center;justify-content:center}
.cart{left:912px;top:22px;width:87px;height:31px;border-radius:16px;background:var(--brown);color:#fff;font-size:11px;font-weight:600;display:flex;align-items:center;justify-content:center;gap:6px}

/* hero */
.hero{left:0;top:75px;width:1200px;height:375px;overflow:hidden}
.hero-left{left:0;top:0;width:1200px;height:375px;background:linear-gradient(135deg,#8a5a33,#b98a5c 45%,#c9b7a0 70%,#7b5534)}
.hero-right{left:0;top:0;width:1200px;height:375px;background:linear-gradient(160deg,#f2f0ec,#d9d4cc 55%,#b88a5a);clip-path:polygon(660px 0,1200px 0,1200px 375px,540px 375px)}
.hero-banner{left:0;top:0;width:1200px;height:375px;background:#fff;clip-path:polygon(440px 156px,795px 156px,765px 216px,408px 216px)}
.hero-title{left:0;width:1200px;text-align:center;font-size:31px;font-weight:700;color:var(--brown-dark)}
.arrow{width:31px;height:31px;border-radius:50%;background:#fff;display:flex;align-items:center;justify-content:center;box-shadow:0 1px 4px rgba(0,0,0,.25)}

/* intro */
.rule{left:200px;width:800px;border-top:1px dashed var(--line)}
.intro-head{top:526px;font-size:24px;line-height:28px;color:var(--brown-dark);font-weight:400}
.intro-head b{font-weight:700}
.intro-text{top:623px;font-size:10px;line-height:15px;color:var(--ink)}
.btn-outline{height:30px;border:1.5px solid var(--brown);border-radius:16px;background:#fff;color:var(--brown);font-size:11px;font-weight:600;display:flex;align-items:center;justify-content:center}
.btn-solid{height:30px;border-radius:16px;background:var(--brown);color:#fff;font-size:11px;font-weight:600;display:flex;align-items:center;justify-content:center}
.divider{left:0;top:818px;width:1200px;height:8px;background:linear-gradient(#f0f0f0,#fff)}

.section-title{font-size:23px;font-weight:600;color:var(--brown-dark)}

/* products */
.product{top:931px;width:181px;height:262px;border:1px solid #e0dcd8;background:#fff}
.product-photo{left:0;top:0;width:179px;height:168px}
.product-name{left:0;top:180px;width:179px;text-align:center;font-size:10px;line-height:16px;color:var(--ink)}
.product-price{left:0;top:218px;width:179px;text-align:center;font-size:12px;font-weight:700}
.product-btn{top:249px;width:113px}

/* cabinetry */
.sage{left:0;top:1271px;width:1200px;height:638px;background:var(--sage)}
.tile{position:absolute}

/* cnc */
.post{top:2020px;width:181px}
.post-photo{width:181px;height:181px}
.post-title{margin-top:25px;font-size:14.5px;line-height:17px;font-weight:500;color:var(--ink)}
.post-body{margin-top:11px;font-size:12px;line-height:13.5px;color:var(--muted)}
.post-more{margin-top:14px;font-size:12px;font-weight:600;color:var(--brown);display:flex;align-items:center;gap:6px}

/* quote */
.quote{left:0;top:2411px;width:1200px;height:350px;background:var(--navy)}
.field{position:absolute;background:#fff;border-radius:12px;font-size:9px;color:#777;padding:7px 12px}

/* footer */
.footer{left:0;top:2761px;width:1200px;height:340px;background:var(--footer)}
.foot-brand{left:200px;top:2862px;font-size:28px;font-weight:700;color:var(--brown);display:flex;align-items:center;gap:10px;white-space:nowrap}
.foot-brand .brand-mark{width:16px;height:16px}
.foot-head{font-size:12px;font-weight:600;color:var(--ink);letter-spacing:.3px}
.foot-text{font-size:11px;color:var(--muted);line-height:15px}
.links a{display:block;font-size:10px;color:var(--muted);text-decoration:none;line-height:19px}
.social{left:970px;width:30px;height:30px;border:1.5px solid var(--brown);border-radius:50%}
.social.filled{background:var(--brown)}
.bottom-rule{left:200px;top:3034px;width:800px;border-top:1px solid #d3d0cc}
.copy{top:3062px;font-size:10px;color:var(--muted);letter-spacing:.3px}
.copy b{color:var(--brown);font-weight:600}
</style>
</head>
<body>

<!-- header -->
<div class="abs brand"><span class="brand-mark"></span>Cobbleford Works</div>
<nav class="abs nav" style="left:0;top:31px">
  <a class="active" style="left:407px">Home</a>
  <a style="left:463px">About Us</a>
  <a style="left:535px">Services</a>
  <a style="left:604px">FAQs</a>
  <a style="left:656px">Contact Us</a>
</nav>
<div class="abs call">Call: 555-014-2290</div>
<div class="abs icon-btn"><svg width="12" height="10" viewBox="0 0 12 10"><rect x="0.5" y="0.5" width="11" height="9" rx="1.5" fill="var(--brown)"/><path d="M1 1.5l5 4 5-4" stroke="#fff" fill="none"/></svg></div>
<div class="abs cart"><svg width="12" height="11" viewBox="0 0 12 11"><path d="M0 1h2l1.6 6h6.4l1.5-4.5H3" fill="#fff"/><circle cx="4.5" cy="9.5" r="1.1" fill="#fff"/><circle cx="9" cy="9.5" r="1.1" fill="#fff"/></svg>$0.00</div>

<!-- hero -->
<section class="abs hero">
  <div class="abs hero-left" role="img" aria-label="Photo of a warm wood kitchen with a granite island"></div>
  <div class="abs hero-right" role="img" aria-label="Photo of a white kitchen with a wood range hood"></div>
  <div class="abs hero-banner"></div>
  <div class="abs hero-title" style="top:165px">Custom Cabinetry</div>
  <div class="abs arrow" style="left:168px;top:171px"><svg width="8" height="10"><path d="M6 1L2 5l4 4" stroke="#333" stroke-width="1.6" fill="none"/></svg></div>
  <div class="abs arrow" style="left:1000px;top:171px"><svg width="8" height="10"><path d="M2 1l4 4-4 4" stroke="#333" stroke-width="1.6" fill="none"/></svg></div>
</section>

<!-- intro -->
<div class="abs rule" style="top:512px"></div>
<h1 class="abs center intro-head"><b>Cobbleford Works</b> is a <b>custom cabinetry, precision wood cutting</b><br>and <b>custom wood art</b> company.</h1>
<div class="abs rule" style="top:598px"></div>
<p class="abs center intro-text">It is a long established fact that a reader will be distracted by the readable content of a page when looking at its layout.<br>The point of using Lorem Ipsum is that it has a more-or-less normal distribution of letters, as opposed to using 'Content here, content here',<br>making it look like readable English. Many desktop publishing packages and web page editors now use Lorem Ipsum as their default model text,<br>and a search for 'lorem ipsum' will uncover many web sites still in their infancy. Various versions have evolved over the years,<br>sometimes by accident, sometimes on purpose (injected humour and the like).</p>
<a class="abs btn-outline" style="left:537px;top:726px;width:125px">Discover About</a>
<div class="abs divider"></div>

<!-- newest creations -->
<h2 class="abs center section-title" style="top:878px">Newest Creations</h2>
<article class="abs product" style="left:200px">
  <div class="abs product-photo" role="img" aria-label="Photo of a carved wooden sign on a CNC machine" style="background:linear-gradient(135deg,#3a3634,#7a5a40 50%,#d8d4d0)"></div>
  <p class="abs product-name">Variations of passages work<br>there are many site</p>
  <p class="abs product-price">$150.99</p>
  <a class="abs btn-outline product-btn" style="left:33px">Shop Now!</a>
</article>
<article class="abs product" style="left:406px">
  <div class="abs product-photo" role="img" aria-label="Photo of a carved wooden flag with an eagle" style="background:linear-gradient(135deg,#5a4a3e,#8d7766 50%,#4b3d33)"></div>
  <p class="abs product-name">Variations of passages work<br>there are many site</p>
  <p class="abs product-price">$150.99</p>
  <a class="abs btn-solid product-btn" style="left:33px">Shop Now!</a>
</article>
<article class="abs product" style="left:612px">
  <div class="abs product-photo" role="img" aria-label="Photo of two carved wooden tap handles" style="background:linear-gradient(135deg,#6b6e72,#c58f5a 50%,#3c3f44)"></div>
  <p class="abs product-name">Variations of passages work<br>there are many site</p>
  <p class="abs product-price">$150.99</p>
  <a class="abs btn-outline product-btn" style="left:33px">Shop Now!</a>
</article>
<article class="abs product" style="left:818px">
  <div class="abs product-photo" role="img" aria-label="Photo of an engraved live-edge wood slab" style="background:linear-gradient(135deg,#7a3c22,#b4714a 50%,#8c4a2c)"></div>
  <p class="abs product-name">Variations of passages work<br>there are many site</p>
  <p class="abs product-price">$150.99</p>
  <a class="abs btn-outline product-btn" style="left:33px">Shop Now!</a>
</article>

<!-- custom cabinetry -->
<section class="abs sage">
  <h2 class="abs center section-title" style="top:57px">Custom Cabinetry</h2>
  <div class="tile" role="img" aria-label="Photo of a white mudroom cabinet with hooks" style="left:200px;top:112px;width:250px;height:188px;background:linear-gradient(135deg,#c7c3bd,#f2f1ef 50%,#bfa27f)"></div>
  <div class="tile" role="img" aria-label="Photo of a wood kitchen with a ceiling fan" style="left:475px;top:112px;width:251px;height:401px;background:linear-gradient(180deg,#e9e8e6,#d9d6d2 40%,#a8743f 70%,#8a6444)"></div>
  <div class="tile" role="img" aria-label="Photo of built-in wood shelving with a ladder" style="left:750px;top:112px;width:250px;height:188px;background:linear-gradient(135deg,#b88955,#d9b488 50%,#6a4a32)"></div>
  <div class="tile" role="img" aria-label="Photo of a cutting board drawer in a wood cabinet" style="left:200px;top:325px;width:250px;height:188px;background:linear-gradient(135deg,#4a4340,#b07a4a 50%,#e0cfb5)"></div>
  <div class="tile" role="img" aria-label="Photo of a rustic wood entry cabinet with a door" style="left:750px;top:325px;width:250px;height:188px;background:linear-gradient(135deg,#e9e7e3,#8d6240 50%,#5c3f2a)"></div>
  <a class="abs btn-solid" style="left:537px;top:543px;width:125px;background:var(--navy)">Request A Quote</a>
</section>

<!-- cnc -->
<h2 class="abs center section-title" style="top:1967px">CNC Precision Wood Cutting</h2>
<article class="abs post" style="left:200px">
  <div class="post-photo" role="img" aria-label="Photo of a wooden dinosaur model in a workshop" style="background:linear-gradient(135deg,#8a7f74,#d9c7a8 50%,#5a5048)"></div>
  <h3 class="post-title">Contrary to popular lorem<br>belief, lorem ipsum</h3>
  <p class="post-body">There are many variations of<br>passages of lorem Ipsum avail-<br>able, but the majority have<br>suffered alteration ...</p>
  <a class="post-more">Read More <svg width="9" height="7"><path d="M0 3.5h8M5 1l3 2.5L5 6" stroke="var(--brown)" fill="none"/></svg></a>
</article>
<article class="abs post" style="left:406px">
  <div class="post-photo" role="img" aria-label="Photo of CNC-cut plywood shapes on a machine bed" style="background:linear-gradient(135deg,#3c5a8a,#e3d6bf 40%,#c9b795)"></div>
  <h3 class="post-title">Contrary to popular lorem<br>belief, lorem ipsum</h3>
  <p class="post-body">There are many variations of<br>passages of lorem Ipsum avail-<br>able, but the majority have<br>suffered alteration ...</p>
  <a class="post-more">Read More <svg width="9" height="7"><path d="M0 3.5h8M5 1l3 2.5L5 6" stroke="var(--brown)" fill="none"/></svg></a>
</article>
<article class="abs post" style="left:612px">
  <div class="post-photo" role="img" aria-label="Photo of a dovetailed plywood box in a shop" style="background:linear-gradient(180deg,#9a9794,#e8e2d6 50%,#b49a78)"></div>
  <h3 class="post-title">Contrary to popular lorem<br>belief, lorem ipsum</h3>
  <p class="post-body">There are many variations of<br>passages of lorem Ipsum avail-<br>able, but the majority have<br>suffered alteration ...</p>
  <a class="post-more">Read More <svg width="9" height="7"><path d="M0 3.5h8M5 1l3 2.5L5 6" stroke="var(--brown)" fill="none"/></svg></a>
</article>
<article class="abs post" style="left:818px">
  <div class="post-photo" role="img" aria-label="Photo of cabinet door panels cut on a CNC table" style="background:linear-gradient(135deg,#3c5a8a,#d9cdb8 40%,#efe8dc)"></div>
  <h3 class="post-title">Contrary to popular lorem<br>belief, lorem ipsum</h3>
  <p class="post-body">There are many variations of<br>passages of lorem Ipsum avail-<br>able, but the majority have<br>suffered alteration ...</p>
  <a class="post-more">Read More <svg width="9" height="7"><path d="M0 3.5h8M5 1l3 2.5L5 6" stroke="var(--brown)" fill="none"/></svg></a>
</article>

<!-- quote form -->
<section class="abs quote">
  <h2 class="abs center section-title" style="top:59px;color:#fff">Request A Quote</h2>
  <div class="field" style="left:294px;top:112px;width:194px;height:24px">Your Name</div>
  <div class="field" style="left:503px;top:112px;width:194px;height:24px">Email</div>
  <div class="field" style="left:713px;top:112px;width:194px;height:24px">Phone</div>
  <div class="field" style="left:294px;top:153px;width:613px;height:82px;padding-top:10px">Message ...</div>
  <a class="abs btn-solid" style="left:557px;top:248px;width:87px">Submit</a>
</section>

<!-- footer -->
<footer class="abs footer"></footer>
<div class="abs foot-brand"><span class="brand-mark"></span>Cobbleford Works</div>
<div class="abs" style="left:549px;top:2821px">
  <h4 class="foot-head">Contact Us</h4>
  <p class="foot-text" style="margin-top:14px;font-size:12px">Call Us: (555) 014-2291</p>
  <p class="foot-text" style="font-size:10.5px">Email: hello@cobblefordworks.com</p>
  <p class="foot-text" style="margin-top:14px;font-size:10px;font-weight:600;color:var(--ink)">Address:</p>
  <p class="foot-text" style="font-size:10px">418 Alder Creek Road Brookhaven,<br>KT 20418</p>
</div>
<div class="abs links" style="left:819px;top:2821px">
  <h4 class="foot-head" style="margin-bottom:10px">Quick Links</h4>
  <a>Home</a><a>About Us</a><a>Services</a><a>FAQs</a><a>Contact Us</a>
</div>
<div class="abs social" style="top:2824px" aria-label="Social link 1"></div>
<div class="abs social filled" style="top:2862px" aria-label="Social link 2"></div>
<div class="abs social" style="top:2900px" aria-label="Social link 3"></div>
<div class="abs social" style="top:2937px" aria-label="Social link 4"></div>
<div class="abs bottom-rule"></div>
<p class="abs center copy">© 2021 <b>Cobbleford Works.</b> All Right Reserved &nbsp;&nbsp;&nbsp;|&nbsp;&nbsp;&nbsp; Terms and Conditions &nbsp;&nbsp;&nbsp;|&nbsp;&nbsp;&nbsp; Privacy Policy</p>
<svg class="abs" style="left:1092px;top:3059px" width="15" height="17" viewBox="0 0 15 17"><path d="M7.5 0L15 17 7.5 12 0 17z" fill="var(--brown-dark)"/></svg>

</body>
</html>
```